Business card and stationary for a garage
Motorwerkplaats Lindeveld
@ph - changes done .Please check and confirm.- Thanks
@quickdraft
Can you please make another version with #136 as the front and #135 as the back side.
Note 1: Please omit the word "Services" and make the logo a little bit bigger at the back side
Note 2: It's Merelhoflaan
Note 3: #135 the back side. The text "Motorwerkplaats Lindeveld" is too gray. Just use the original logo and colors.
#ALL
Please use "T" for phonenumber and "F" for fax. Do not use the English abbreviations. Or better use icons.
Nice designs, thank you.
We dont prefer a style like #124-#129 for the back of the card. Its to simple. The service listing can be more attractive like in #121 or #118 (horizontal).
#ALL please do not use english words in business card like "Our services". Use only "Services" as this is also a common word in Dutch.
"Voor alle merken" means "For all brands"

```html
<!DOCTYPE html>
<html lang="nl">
<head>
<meta charset="utf-8">
<title>Motorwerkplaats Lindeveld – visitekaartjes</title>
<link rel="stylesheet" href="https://fonts.googleapis.com/css2?family=Arimo:wght@400;700&display=swap">
<style>
  :root {
    --stage: #e9e6e2;
    --paper: #ffffff;
    --ink: #2b2b2b;
    --ink-soft: #6d6d6d;
    --night: #0c0c0c;
    --night-soft: #8a8a8a;
    --red: #d7141b;
    --red-deep: #7d0a0e;
    --rule-light: #cfcfcf;
    --rule-dark: #3a3a3a;
  }
  * { margin: 0; padding: 0; box-sizing: border-box; }
  html, body { width: 1200px; height: 811px; overflow: hidden; }
  body {
    background: var(--stage);
    font-family: "Arimo", Arial, sans-serif;
    position: relative;
  }
  .card {
    position: absolute;
    width: 490px;
    height: 276px;
    border-radius: 14px;
    overflow: hidden;
    box-shadow: 0 6px 14px rgba(0,0,0,.28);
  }
  .card--light { background: var(--paper); color: var(--ink); }
  .card--dark { background: radial-gradient(ellipse at 50% 35%, #262626 0%, var(--night) 70%); color: var(--night-soft); }
  .opt1 { left: 80px; }
  .opt2 { left: 630px; }
  .front { top: 96px; }
  .back { top: 400px; }

  .brand {
    position: absolute;
    display: flex;
    align-items: center;
    gap: 10px;
    font-weight: 700;
    text-transform: uppercase;
    letter-spacing: .5px;
  }
  .brand__mark { width: 16px; height: 16px; background: var(--red); flex: none; }
  .card--light .brand { color: var(--ink); }
  .card--dark .brand { color: #d9d9d9; }
  .front .brand { top: 60px; left: 0; right: 0; justify-content: center; font-size: 22px; }
  .back .brand { top: 100px; left: 26px; width: 262px; font-size: 19px; line-height: 1.2; }

  .holder {
    position: absolute;
    left: 36px; top: 134px;
    font-size: 20px;
    font-weight: 700;
    color: var(--red);
  }
  .divider { position: absolute; width: 1px; }
  .card--light .divider { background: var(--rule-light); }
  .card--dark .divider { background: var(--rule-dark); }
  .front .divider { left: 206px; top: 124px; height: 96px; }
  .back .divider { left: 300px; top: 84px; height: 140px; }

  .contact {
    position: absolute;
    left: 222px; top: 122px;
    list-style: none;
    font-size: 13px;
    line-height: 19px;
  }
  .contact li { display: flex; align-items: center; gap: 8px; }
  .contact li.cont { padding-left: 20px; }
  .contact svg { width: 12px; height: 12px; fill: var(--red); flex: none; }
  .card--light .contact { color: var(--ink); }
  .card--dark .contact { color: var(--night-soft); }

  .services { position: absolute; left: 316px; top: 82px; }
  .services__title { font-size: 19px; color: var(--red); margin-bottom: 4px; }
  .services__list { list-style: none; font-size: 14px; line-height: 20px; }
  .card--light .services__list { color: var(--ink-soft); }
  .card--dark .services__list { color: var(--night-soft); }

  .footer-band {
    position: absolute;
    left: 0; right: 0;
    bottom: 20px;
    height: 18px;
    display: flex;
  }
  .footer-band__lead { width: 64px; background: linear-gradient(90deg, #111 0%, #6e6e6e 55%, #1a1a1a 100%); }
  .footer-band__web {
    flex: 1;
    background: linear-gradient(90deg, rgba(215,20,27,0) 0%, var(--red-deep) 30%, var(--red) 100%);
    color: #fff;
    font-size: 11px;
    font-weight: 700;
    text-align: right;
    padding-right: 14px;
    line-height: 18px;
  }
  .card--light .footer-band__web { background: linear-gradient(90deg, #ffffff 0%, var(--red-deep) 45%, var(--red) 100%); }

  .option-label {
    position: absolute;
    top: 704px;
    width: 490px;
    text-align: center;
    font-size: 20px;
    color: #555;
  }
</style>
</head>
<body>

  <section class="card card--light front opt1">
    <div class="brand"><span class="brand__mark"></span>Motorwerkplaats Lindeveld</div>
    <p class="holder">Ruben Hoekstra</p>
    <span class="divider"></span>
    <ul class="contact">
      <li><svg viewBox="0 0 12 12"><path d="M2 1l2 0 1 3-1.5 1a6 6 0 0 0 3.5 3.5L8 7l3 1v2a1 1 0 0 1-1 1A9 9 0 0 1 1 2a1 1 0 0 1 1-1z"/></svg>030-4172286</li>
      <li><svg viewBox="0 0 12 12"><path d="M3 1h5v3H3zM1 5h10v5H9v1H3v-1H1zM4 8h4v3H4z"/></svg>030-4172287</li>
      <li><svg viewBox="0 0 12 12"><path d="M1 3h10v7H1zM1 3l5 4 5-4"/></svg>info@motorwerkplaatslindeveld.nl</li>
      <li><svg viewBox="0 0 12 12"><path d="M6 1l5 5H9.5v5h-2V8h-3v3h-2V6H1z"/></svg>Merelhoflaan 20</li>
      <li class="cont">3811 KD Lindeveld</li>
    </ul>
    <div class="footer-band"><span class="footer-band__lead"></span><span class="footer-band__web">www.motorwerkplaatslindeveld.nl</span></div>
  </section>

  <section class="card card--light back opt1">
    <div class="brand"><span class="brand__mark"></span>Motorwerkplaats Lindeveld</div>
    <span class="divider"></span>
    <div class="services">
      <p class="services__title">Services</p>
      <ul class="services__list"><li>Onderhoud</li><li>APK</li><li>Banden</li><li>Airco</li><li>Voor alle merken</li></ul>
    </div>
    <div class="footer-band"><span class="footer-band__lead"></span><span class="footer-band__web">www.motorwerkplaatslindeveld.nl</span></div>
  </section>

  <section class="card card--dark front opt2">
    <div class="brand"><span class="brand__mark"></span>Motorwerkplaats Lindeveld</div>
    <p class="holder">Ruben Hoekstra</p>
    <span class="divider"></span>
    <ul class="contact">
      <li><svg viewBox="0 0 12 12"><path d="M2 1l2 0 1 3-1.5 1a6 6 0 0 0 3.5 3.5L8 7l3 1v2a1 1 0 0 1-1 1A9 9 0 0 1 1 2a1 1 0 0 1 1-1z"/></svg>030-4172286</li>
      <li><svg viewBox="0 0 12 12"><path d="M3 1h5v3H3zM1 5h10v5H9v1H3v-1H1zM4 8h4v3H4z"/></svg>030-4172287</li>
      <li><svg viewBox="0 0 12 12"><path d="M1 3h10v7H1zM1 3l5 4 5-4"/></svg>info@motorwerkplaatslindeveld.nl</li>
      <li><svg viewBox="0 0 12 12"><path d="M6 1l5 5H9.5v5h-2V8h-3v3h-2V6H1z"/></svg>Merelhoflaan 20</li>
      <li class="cont">3811 KD Lindeveld</li>
    </ul>
    <div class="footer-band"><span class="footer-band__lead"></span><span class="footer-band__web">www.motorwerkplaatslindeveld.nl</span></div>
  </section>

  <section class="card card--dark back opt2">
    <div class="brand"><span class="brand__mark"></span>Motorwerkplaats Lindeveld</div>
    <span class="divider"></span>
    <div class="services">
      <p class="services__title">Services</p>
      <ul class="services__list"><li>Onderhoud</li><li>APK</li><li>Banden</li><li>Airco</li><li>Voor alle merken</li></ul>
    </div>
    <div class="footer-band"><span class="footer-band__lead"></span><span class="footer-band__web">www.motorwerkplaatslindeveld.nl</span></div>
  </section>

  <p class="option-label opt1">Option 1</p>
  <p class="option-label opt2">Option 2</p>

</body>
</html>
```